IT services company needs a business card designed

-2 sided business card.-Front is going to be the logo raised (3D floating effect) on a black background. Make the logos spider web shiny silver and keep the spider the same design. -Back needs to have the following information:Doug Farrow, Managing Partner, Cell: 602-488-3179, Website: Kolvantra.com, Email: Doug@Kolvantra.com
Target Market(s)
IT Services
Industry/Entity Type
It Company
Contact Information for Business Card
-2 sided business card.
-Front is going to be the logo raised (3D floating effect) on a black background. Make the logos spider web shiny silver and keep the spider the same design.
-Back needs to have the following information:
Doug Farrow, Managing Partner, Cell: 602-488-3179, Website: Kolvantra.com, Email: Doug@Kolvantra.com
Look and feel

```html
<!DOCTYPE html>
<html lang="en">
<head>
<meta charset="utf-8">
<title>Kolvantra — Business Card</title>
<link href="https://fonts.googleapis.com/css2?family=Roboto:wght@400;500;700&display=swap" rel="stylesheet">
<style>
  :root {
    --page-bg: #232323;
    --card-bg: #141414;
    --card-edge: #2a2a2a;
    --silver: #d8d8d8;
    --muted: #bdbdbd;
    --accent: #3f86cf;
    --rule: #6b6b6b;
    --web-tone-a: #1a1a1a;
    --web-tone-b: #111111;
  }
  html, body {
    margin: 0;
    width: 1200px;
    height: 1017px;
    overflow: hidden;
    background: var(--page-bg);
    font-family: "Roboto", Arial, sans-serif;
  }
  .sheet {
    position: relative;
    width: 1200px;
    height: 1017px;
  }
  .card {
    position: absolute;
    left: 310px;
    width: 580px;
    height: 331px;
    background: var(--card-bg);
    border: 1px solid var(--card-edge);
    box-sizing: border-box;
    overflow: hidden;
  }
  .card--front { top: 150px; }
  .card--back  { top: 536px; }

  /* Front */
  .front-texture {
    position: absolute;
    inset: 0;
    background: radial-gradient(ellipse at 60% 40%, var(--web-tone-a), var(--web-tone-b) 75%);
  }
  .front-mark {
    position: absolute;
    left: 0; right: 0;
    top: 50%;
    transform: translateY(-50%);
    text-align: center;
    font-size: 40px;
    font-weight: 500;
    letter-spacing: 4px;
    color: var(--silver);
    text-transform: uppercase;
  }

  /* Back */
  .brand {
    position: absolute;
    right: 36px;
    top: 48px;
    display: flex;
    align-items: center;
    gap: 10px;
    font-size: 30px;
    font-weight: 500;
    letter-spacing: 1px;
    color: var(--silver);
    text-transform: uppercase;
  }
  .brand__dot {
    width: 12px; height: 12px;
    background: var(--accent);
    border-radius: 50%;
  }
  .top-rule {
    position: absolute;
    left: 36px; right: 36px;
    top: 108px;
    height: 1px;
    background: var(--rule);
  }
  .website {
    position: absolute;
    right: 36px;
    top: 122px;
    font-size: 13px;
    letter-spacing: 1px;
    color: var(--muted);
  }
  .person {
    position: absolute;
    left: 36px;
    top: 196px;
  }
  .person__name {
    font-size: 20px;
    font-weight: 700;
    color: var(--accent);
    text-transform: uppercase;
    letter-spacing: 0.5px;
  }
  .person__role {
    font-size: 13px;
    font-weight: 500;
    color: var(--muted);
    text-transform: uppercase;
    letter-spacing: 0.5px;
    margin-top: 2px;
  }
  .person__rule {
    width: 200px;
    height: 1px;
    background: var(--rule);
    margin: 8px 0 10px;
  }
  .contact {
    list-style: none;
    margin: 0;
    padding: 0;
  }
  .contact__item {
    display: flex;
    align-items: center;
    gap: 10px;
    font-size: 14px;
    color: var(--muted);
    margin-bottom: 5px;
  }
  .contact__icon {
    width: 14px; height: 14px;
    flex: none;
  }
</style>
</head>
<body>
<main class="sheet">

  <section class="card card--front" aria-label="Business card front">
    <div class="front-texture" role="img" aria-label="Faint embossed web pattern across the black card"></div>
    <div class="front-mark">Kolvantra</div>
  </section>

  <section class="card card--back" aria-label="Business card back">
    <div class="brand"><span class="brand__dot"></span>Kolvantra</div>
    <div class="top-rule"></div>
    <div class="website">www.Kolvantra.com</div>

    <div class="person">
      <div class="person__name">Doug Farrow</div>
      <div class="person__role">Managing Partner</div>
      <div class="person__rule"></div>
      <ul class="contact">
        <li class="contact__item">
          <svg class="contact__icon" viewBox="0 0 14 14" aria-hidden="true">
            <rect x="3" y="1" width="8" height="12" rx="1.5" fill="none" stroke="#3f86cf" stroke-width="1.4"/>
            <line x1="6" y1="11" x2="8" y2="11" stroke="#3f86cf" stroke-width="1.2"/>
          </svg>
          602-488-3179
        </li>
        <li class="contact__item">
          <svg class="contact__icon" viewBox="0 0 14 14" aria-hidden="true">
            <rect x="1" y="3" width="12" height="8" fill="none" stroke="#3f86cf" stroke-width="1.4"/>
            <polyline points="1,3 7,8 13,3" fill="none" stroke="#3f86cf" stroke-width="1.4"/>
          </svg>
          Doug@Kolvantra.com
        </li>
      </ul>
    </div>
  </section>

</main>
</body>
</html>
```